Brochure Design

We are looking for a brochure design that describes our credit repair and restoration business.
One of the files that has been uploaded is "TRV Presentation Guidebook". This provides information about our service and snippets can be used for the text in the brochure.
I also uploaded several examples of brochures that we liked.
Target Market(s)
The target market is consumers, not businesses, who are considering our credit repair and restoration service.
Industry/Entity Type
Business
Requirements
Must have
- We want a brochure that is rich with color, and pictures of families and business people. Large pictures that span the entire length of the brochure, or several panels is preferred. The color scheme should be black and blue based
Nice to have
- A stylized representation of our logo. Our logo is not important to be included in the primary design scheme, because our logo is not stylistic enough from what we currently have. However, a stylized version of our logo that can be integrated into the design in some way would be wonderful. We will attached a pic of our design. It is pretty basic and there are many stock photos or art that can be used to offer a more stylized version of our logo to incorporate into the design.
Should not have
- The primary focus of the brochure is a professional design with plenty of color and pictures. This is not designed to necessarily be an informative brochure, but more of a "business presence" brochure. So there is not a need to provide a lot of space for text. Certainly there should be enough text to describe our business and make some bullet points, but text explanation is not the focus.

```html
<!DOCTYPE html>
<html lang="en">
<head>
<meta charset="utf-8">
<title>TRV Credit – Tri-fold Brochure</title>
<link href="https://fonts.googleapis.com/css2?family=Bebas+Neue&family=Roboto:wght@400;700&display=swap" rel="stylesheet">
<style>
  :root {
    --page-bg: #d9d9d9;
    --black: #0b0b0c;
    --black-soft: #26272a;
    --blue-deep: #0a3f86;
    --blue: #1560bd;
    --blue-bright: #2a7fd8;
    --cyan: #29a8e6;
    --white: #ffffff;
    --text-light: #e6eef8;
    --photo-warm: #c9a574;
  }
  * { box-sizing: border-box; margin: 0; padding: 0; }
  html, body { width: 1200px; height: 1080px; overflow: hidden; }
  body {
    background: radial-gradient(ellipse at center, #f2f2f2 0%, var(--page-bg) 100%);
    font-family: "Roboto", Arial, sans-serif;
    position: relative;
  }
  .brochure {
    position: absolute;
    left: 120px; top: 40px;
    width: 960px; height: 1000px;
    display: grid;
    grid-template-columns: repeat(3, 320px);
    grid-template-rows: 440px 560px;
    box-shadow: 0 10px 30px rgba(0,0,0,.25);
  }
  .hero-photo {
    grid-column: 1 / 3; grid-row: 1;
    background:
      radial-gradient(ellipse 30% 55% at 62% 55%, #5a3a26 0%, rgba(90,58,38,0) 70%),
      linear-gradient(90deg, #b79a72 0%, #d8c9ad 25%, #e8dcc4 45%, var(--photo-warm) 70%, #8a6a44 100%);
  }
  .brand-panel {
    grid-column: 3; grid-row: 1;
    background: var(--black);
    color: var(--white);
    display: flex; flex-direction: column; align-items: center; justify-content: flex-end;
    padding: 0 12px 64px;
    text-align: center;
  }
  .brand-mark { width: 60px; height: 60px; background: var(--blue-bright); margin-bottom: 70px; }
  .brand-name {
    font-family: "Bebas Neue", Impact, sans-serif; font-weight: 400;
    font-size: 68px; line-height: 1; letter-spacing: 1px;
  }
  .brand-tagline {
    font-family: "Bebas Neue", Impact, sans-serif; font-weight: 400;
    font-size: 22px; letter-spacing: .5px; margin-top: 4px; white-space: nowrap;
  }
  .panel { grid-row: 2; padding: 18px 20px; color: var(--white); }
  .panel-benefits { grid-column: 1; background: linear-gradient(160deg, var(--black) 0%, var(--black-soft) 100%); }
  .panel-disputes { grid-column: 2; background: linear-gradient(160deg, var(--blue) 0%, var(--blue-deep) 100%); }
  .panel-fees { grid-column: 3; background: linear-gradient(160deg, var(--blue-deep) 0%, var(--blue) 60%, var(--blue-bright) 100%); }
  .section-title {
    font-family: "Bebas Neue", Impact, sans-serif; font-weight: 400;
    font-size: 44px; line-height: .98; margin: 8px 0 40px; white-space: nowrap;
  }
  .label {
    display: inline-block;
    font-family: "Bebas Neue", Impact, sans-serif; font-weight: 400;
    font-size: 27px; line-height: 1.05;
    padding: 5px 12px 3px;
  }
  .label-cyan { background: var(--cyan); color: var(--white); margin-left: -20px; padding-left: 20px; }
  .label-black { background: var(--black); color: var(--white); }
  .copy {
    font-size: 13px; line-height: 1.35; text-align: justify;
    color: var(--text-light);
    margin: 10px 0 18px;
  }
  .panel-benefits .copy { margin-bottom: 30px; }
  .panel-fees .block-refund { margin-top: 70px; }
</style>
</head>
<body>
  <main class="brochure">
    <div class="hero-photo" role="img" aria-label="Photo of a smiling young woman with a shoulder bag in a bright, softly blurred classroom"></div>

    <section class="brand-panel">
      <div class="brand-mark"></div>
      <h1 class="brand-name">TRV CREDIT</h1>
      <p class="brand-tagline">Better credit. Brighter future!</p>
    </section>

    <section class="panel panel-benefits">
      <h2 class="section-title">What you get at<br>TRV Credit:</h2>
      <h3 class="label label-cyan">Highly Skilled Staff</h3>
      <p class="copy"><strong>TRV CREDIT's</strong> staff is composed of a group of Accountants, Attorneys and Loan Officers. This gives us a huge arsenal of information. In addition, we are constantly monitoring laws about credit reporting and adjusting our methods. TRV CREDIT eats, sleeps and thinks about repairing bad credit. Lucky for our clients!</p>
      <h3 class="label label-cyan">No Form Letters</h3>
      <p class="copy">We NEVER use form letters. Many so called credit repair firms will use the same letter for ALL their clients. This proves ineffective. Our legal department will prepare custom disputes.</p>
    </section>

    <section class="panel panel-disputes">
      <h3 class="label label-black">Unlimited Disputes</h3>
      <p class="copy">Unlike other companies that charge you a fee for each dispute, we offer unlimited disputes at no additional cost. You pay one flat monthly fee, whether it be 10 disputes or 100. We will dispute with the Credit Bureaus as well as the problem creditors or collection companies.</p>
      <h3 class="label label-black">Unlimited Deletions</h3>
      <p class="copy">Some credit companies charge you a fee for each individual deletion. Our process is geared to protecting your rights. You will never be charged extra for simply doing the job you hired us to do.</p>
      <h3 class="label label-black">No Hidden Fees</h3>
      <p class="copy">Our service is built around being effective and being easy for you. As a result, what you see is what you get. THERE ARE NO HIDDEN FEES. You have enough to worry about in your regular life without having to wonder where the catch is. We are here to make this process easy and free of worry.</p>
    </section>

    <section class="panel panel-fees">
      <div class="block-fee">
        <h3 class="label label-black">Low Monthly Fee</h3>
        <p class="copy">Our significant experience in helping clients just like you has allowed us to develop some of the most effective strategies and procedures available. As a result, we pass the savings directly to you. The low monthly service fee of $89 takes care of all your services.</p>
      </div>
      <div class="block-refund">
        <h3 class="label label-black">Full Refund Policy/<br>Cancel Anytime</h3>
        <p class="copy">We believe our service is so effective that we offer a complete warranty that entitles you to all or some of your money back if enough disputed items aren't removed from your credit report. Our services are provided on a month-to-month basis, you choose how long or how short a period to employ us. You have the option of canceling at any time, without any extra charges.</p>
      </div>
    </section>
  </main>
</body>
</html>
```